Business Brochure for Mobile Fleet Mechanic Company

Make a brochure for an mobile mechanic company that is a Bi-fold 8.5"Wx11"H. A Bi-fold would have the outside and inside design so it is a total of 4 pages at 8.5"x11". The print is 2-sides 17"Wx11"H that folds down to 8.5"Wx11"H.
Should have photo of mechanic working. Blue in logo is Pantone 284C. Will provide text to be added to approved design.

Contact Information for Business Card

2-sided card using the same design elements and colors as the brochure.

```html
<!DOCTYPE html>
<html lang="en">
<head>
<meta charset="utf-8">
<title>RoadMedic Fleet Brochure</title>
<link href="https://fonts.googleapis.com/css2?family=Oswald:wght@500;700&family=Roboto+Condensed:wght@400;700&display=swap" rel="stylesheet">
<style>
:root{
  --blue:#1f6fb5;
  --blue-deep:#0f4f8c;
  --blue-light:#5aa9e6;
  --ink:#24272c;
  --carbon:#1d2025;
  --carbon-2:#2d3138;
  --paper:#f3f4f6;
  --paper-2:#dcdfe3;
  --stage:#e8e9eb;
  --muted:#5b6068;
}
*{box-sizing:border-box;margin:0;padding:0}
html,body{width:1200px;height:2317px;overflow:hidden;background:var(--stage)}
body{position:relative;font-family:"Roboto Condensed",Arial,sans-serif;color:var(--ink)}
.page{position:absolute;width:550px;height:712px;overflow:hidden;background:linear-gradient(170deg,var(--paper) 0%,#e9ebee 60%,var(--paper-2) 100%)}
.spread{position:absolute;width:1100px;height:712px;box-shadow:0 12px 30px rgba(0,0,0,.18)}
.spread .page{top:0}
.page.left{left:0}
.page.right{left:550px}
.solo{left:325px;top:40px;box-shadow:0 12px 30px rgba(0,0,0,.18)}
.abs{position:absolute}
.brand{position:absolute;display:flex;align-items:center;gap:9px;font-family:"Oswald",sans-serif;font-weight:500;color:var(--blue);font-size:34px;line-height:1}
.brand .mark{width:15px;height:15px;border-radius:50%;background:var(--blue)}
.photo{position:absolute}
.headline{font-family:"Oswald",sans-serif;font-weight:700;text-transform:uppercase;line-height:1}
.icon{width:18px;height:18px;fill:currentColor}
/* cover */
.cover-tag{position:absolute;right:0;top:0;width:330px;height:118px}
.cover-tag .label{position:absolute;right:26px;top:30px;text-align:right;color:var(--blue-light);font-family:"Oswald",sans-serif;font-weight:500;font-size:25px;line-height:1.15;text-transform:uppercase}
.cover-photo{left:0;top:0;width:550px;height:470px;clip-path:polygon(0 150px,220px 118px,550px 118px,550px 440px,0 480px);background:linear-gradient(160deg,#0d2140 0%,#1d4f94 40%,#2a6cc1 60%,#0b1a30 100%)}
.cover-title{position:absolute;left:0;right:30px;top:508px;text-align:right;font-size:46px;color:var(--ink)}
.cover-sub{position:absolute;right:40px;top:566px;font-family:"Oswald",sans-serif;font-weight:500;font-size:14px;color:var(--blue);text-transform:uppercase;letter-spacing:.3px}
.cover-web{position:absolute;left:40px;bottom:34px;font-size:12px;color:var(--muted);letter-spacing:1px}
.band{position:absolute;left:0;bottom:0;width:550px;height:96px}
.phone{position:absolute;display:flex;align-items:center;gap:12px;color:#fff;font-family:"Oswald",sans-serif;font-weight:500;font-size:28px}
.phone .dot{width:34px;height:34px;border-radius:50%;border:2px solid #fff;display:flex;align-items:center;justify-content:center}
/* back page */
.back-head{position:absolute;left:60px;right:30px;top:30px;text-align:center}
.back-head h2{font-family:"Oswald",sans-serif;font-weight:500;color:var(--blue);font-size:24px;text-transform:uppercase}
.back-head p{font-family:"Oswald",sans-serif;font-weight:500;font-size:13px;color:var(--ink);text-transform:uppercase;margin-top:4px}
.back-panel{left:0;top:110px;width:550px;height:602px}
.back-copy{position:absolute;left:48px;top:150px;width:250px;color:#fff}
.back-copy h3{font-family:"Oswald",sans-serif;font-weight:500;color:var(--blue-light);font-size:18px;text-transform:uppercase;margin-bottom:8px}
.back-copy p{font-size:12.5px;line-height:1.35}
.mechanic-photo{left:40px;top:290px;width:190px;height:250px;background:linear-gradient(180deg,#4d5a6c 0%,#273146 55%,#1b2333 100%);border-radius:4px}
.car-photo{left:250px;top:380px;width:260px;height:140px;background:radial-gradient(ellipse at 50% 60%,#f3f4f5 0%,#c8ccd1 45%,#8a9097 80%,rgba(90,96,104,0) 100%)}
.contact{position:absolute;left:40px;top:590px;color:#fff;font-size:16px;line-height:1}
.contact li{list-style:none;display:flex;align-items:center;gap:10px;margin-bottom:9px}
.contact .ico{width:18px;height:18px;border-radius:3px;background:var(--blue-light);display:flex;align-items:center;justify-content:center;color:var(--carbon)}
.contact .ico svg{width:12px;height:12px;fill:currentColor}
/* inside */
.dark-block{left:0;top:0;width:550px;height:400px;background:var(--carbon)}
.inside-copy{position:absolute;left:36px;top:40px;width:370px;color:#fff}
.inside-copy h2{font-family:"Oswald",sans-serif;font-weight:500;color:var(--blue-light);font-size:24px;text-transform:uppercase;margin-bottom:10px}
.inside-copy p{font-size:12.5px;line-height:1.35;margin-bottom:16px}
.ticks li{list-style:none;display:flex;align-items:center;gap:10px;font-family:"Oswald",sans-serif;font-weight:500;font-size:12px;text-transform:uppercase;margin-bottom:9px}
.ticks .box{width:13px;height:13px;border:1.5px solid var(--blue-light);display:flex;align-items:center;justify-content:center;flex:none}
.ticks .box svg{width:9px;height:9px;stroke:var(--blue-light);fill:none;stroke-width:3}
.list-head{position:absolute;left:36px;top:420px;display:flex;align-items:center;gap:8px;font-family:"Oswald",sans-serif;font-weight:500;font-size:16px;text-transform:uppercase;color:var(--ink)}
.list-head span{color:var(--blue);font-size:20px;letter-spacing:-3px}
.service-list{position:absolute;left:60px;top:452px;font-size:11.5px;line-height:1.27;color:var(--muted);list-style:none}
.suv-photo{left:300px;top:470px;width:220px;height:150px;background:radial-gradient(ellipse at 50% 55%,#5a5f66 0%,#2c2f34 45%,rgba(210,213,217,0) 75%)}
.strip{position:absolute;left:0;bottom:0;width:550px;height:20px;background:linear-gradient(90deg,var(--blue-deep),var(--blue))}
.work-photo{left:0;top:0;width:550px;height:400px;background:linear-gradient(120deg,#c9cfd7 0%,#8793a3 40%,#1f3f75 65%,#16305e 100%)}
.right-copy{position:absolute;left:36px;top:420px;width:480px}
.right-copy h2{font-family:"Oswald",sans-serif;font-weight:500;color:var(--blue);font-size:17px;text-transform:uppercase;line-height:1.2;margin-bottom:8px}
.right-copy p{font-size:12.5px;line-height:1.35;color:var(--muted);margin-bottom:12px}
.right-copy .ticks{display:grid;grid-template-columns:1fr 1fr;column-gap:20px}
.right-copy .ticks li{color:var(--ink);margin-bottom:7px}
.right-copy .ticks .box{border-color:var(--blue)}
.right-copy .ticks .box svg{stroke:var(--blue)}
</style>
</head>
<body>
<svg width="0" height="0" style="position:absolute">
  <defs>
    <symbol id="i-phone" viewBox="0 0 24 24"><path d="M6.6 10.8a15 15 0 0 0 6.6 6.6l2.2-2.2a1 1 0 0 1 1-.25 11.4 11.4 0 0 0 3.6.6 1 1 0 0 1 1 1V20a1 1 0 0 1-1 1A17 17 0 0 1 3 4a1 1 0 0 1 1-1h3.5a1 1 0 0 1 1 1c0 1.25.2 2.45.6 3.6a1 1 0 0 1-.25 1z"/></symbol>
    <symbol id="i-mail" viewBox="0 0 24 24"><path d="M2 5h20v14H2z M2 5l10 8 10-8" fill="none" stroke="currentColor" stroke-width="2.4"/></symbol>
    <symbol id="i-web" viewBox="0 0 24 24"><circle cx="12" cy="12" r="9" fill="none" stroke="currentColor" stroke-width="2.4"/><path d="M3 12h18M12 3c3 3 3 15 0 18M12 3c-3 3-3 15 0 18" fill="none" stroke="currentColor" stroke-width="2"/></symbol>
    <symbol id="i-tick" viewBox="0 0 10 10"><path d="M1 5l3 3 5-7"/></symbol>
    <linearGradient id="g-band" x1="0" x2="1"><stop offset="0" stop-color="#0f4f8c"/><stop offset="1" stop-color="#1f6fb5"/></linearGradient>
  </defs>
</svg>

<section class="page solo front-cover">
  <div class="photo cover-photo" role="img" aria-label="Photo of blue fleet trucks parked at night"></div>
  <svg class="cover-tag" viewBox="0 0 330 118"><polygon points="20,0 330,0 330,118 0,118" fill="#2d3138"/><polygon points="20,0 330,0 330,6 18,6" fill="#5aa9e6"/></svg>
  <div class="cover-tag"><div class="label">Full-Service<br>Fleet Maintenance</div></div>
  <div class="brand" style="left:26px;top:54px"><span class="mark"></span>RoadMedic</div>
  <h1 class="headline cover-title">Truck and Auto Repairs</h1>
  <p class="cover-sub">For complete fleet repairs, call us today!</p>
  <svg class="band" viewBox="0 0 550 96"><polygon points="0,70 230,70 260,30 550,20 550,96 0,96" fill="url(#g-band)"/><polygon points="0,64 228,64 258,24 550,14 550,20 260,30 230,70 0,70" fill="#5aa9e6"/></svg>
  <div class="phone" style="right:36px;bottom:22px"><span class="dot"><svg class="icon"><use href="#i-phone"/></svg></span>555 010 2040</div>
  <p class="cover-web">www.roadmedic-demo.com</p>
</section>

<section class="spread outside" style="left:50px;top:800px">
  <div class="page left back-page">
    <div class="back-head">
      <h2>Full-Service Fleet Maintenance</h2>
      <p>Keep your vehicles running</p>
    </div>
    <svg class="abs back-panel" viewBox="0 0 550 602">
      <polygon points="0,0 550,0 550,300 0,440" fill="#1d2025"/>
      <polygon points="300,300 420,0 450,0 330,300" fill="#1f6fb5" opacity=".55"/>
      <polygon points="350,300 470,0 490,0 370,300" fill="#2d3138"/>
      <polygon points="0,440 550,300 550,310 0,450" fill="#5aa9e6"/>
      <polygon points="0,450 270,381 300,602 0,602" fill="#2d3138"/>
    </svg>
    <div class="back-copy">
      <h3>Mobile Fleet Mechanic</h3>
      <p>RoadMedic brings full fleet repairs to your yard, so your trucks stay on the road and off the lift. Our certified techs arrive ready to work. CONTACT US TODAY FOR AN APPOINTMENT.</p>
    </div>
    <div class="photo mechanic-photo" role="img" aria-label="Photo of a smiling mechanic in navy overalls holding a wrench"></div>
    <div class="photo car-photo" role="img" aria-label="Photo of a silver sedan"></div>
    <ul class="contact">
      <li><span class="ico"><svg><use href="#i-phone"/></svg></span>555 010 2040</li>
      <li><span class="ico"><svg><use href="#i-mail"/></svg></span>service@roadmedic-demo.com</li>
      <li><span class="ico"><svg><use href="#i-web"/></svg></span>www.roadmedic-demo.com</li>
    </ul>
    <div class="brand" style="right:30px;bottom:36px;font-size:30px"><span class="mark"></span>RoadMedic</div>
  </div>

  <div class="page right front-cover">
    <div class="photo cover-photo" role="img" aria-label="Photo of blue fleet trucks parked at night"></div>
    <svg class="cover-tag" viewBox="0 0 330 118"><polygon points="20,0 330,0 330,118 0,118" fill="#2d3138"/><polygon points="20,0 330,0 330,6 18,6" fill="#5aa9e6"/></svg>
    <div class="cover-tag"><div class="label">Full-Service<br>Fleet Maintenance</div></div>
    <div class="brand" style="left:26px;top:54px"><span class="mark"></span>RoadMedic</div>
    <h1 class="headline cover-title">Truck and Auto Repairs</h1>
    <p class="cover-sub">For complete fleet repairs, call us today!</p>
    <svg class="band" viewBox="0 0 550 96"><polygon points="0,70 230,70 260,30 550,20 550,96 0,96" fill="url(#g-band)"/><polygon points="0,64 228,64 258,24 550,14 550,20 260,30 230,70 0,70" fill="#5aa9e6"/></svg>
    <div class="phone" style="right:36px;bottom:22px"><span class="dot"><svg class="icon"><use href="#i-phone"/></svg></span>555 010 2040</div>
    <p class="cover-web">www.roadmedic-demo.com</p>
  </div>
</section>

<section class="spread inside" style="left:50px;top:1560px">
  <div class="page left services-page">
    <div class="abs dark-block"></div>
    <svg class="abs" style="left:0;top:0" width="550" height="400" viewBox="0 0 550 400">
      <polygon points="400,400 520,0 545,0 425,400" fill="#8c9097"/>
      <polygon points="440,400 550,40 550,110 462,400" fill="#6a6e75"/>
      <polygon points="470,400 550,140 550,400" fill="#e3e5e8"/>
    </svg>
    <div class="inside-copy">
      <h2>Efficient Fleet Repair</h2>
      <p>Getting repairs done on time for your fleet is a smart investment in your business. Regular maintenance can help prevent downtime, as the team at RoadMedic Services will be able to identify problems before they impact your business. We have a variety of fleet repair options available to handle fleets of any size. Getting the small things taken care of can prevent more expensive repairs down the road.</p>
      <ul class="ticks">
        <li><span class="box"><svg><use href="#i-tick"/></svg></span>Preventative maintenance</li>
        <li><span class="box"><svg><use href="#i-tick"/></svg></span>D.O.T. inspections</li>
        <li><span class="box"><svg><use href="#i-tick"/></svg></span>MD PM inspections</li>
        <li><span class="box"><svg><use href="#i-tick"/></svg></span>All types of mechanical repairs</li>
        <li><span class="box"><svg><use href="#i-tick"/></svg></span>Trailer repairs</li>
      </ul>
    </div>
    <h3 class="list-head"><span>»</span>Full list of auto and truck repair services</h3>
    <ul class="service-list">
      <li>Brakes, alignment, shocks, and struts</li>
      <li>Alternators and batteries</li>
      <li>Starters and water pumps</li>
      <li>Thermostats and radiators</li>
      <li>Hoses, belts, and fuel pumps</li>
      <li>Electrical problems</li>
      <li>CV joints, engines, and transmissions</li>
      <li>Diagnostics</li>
      <li>D.O.T. inspections</li>
      <li>Liftgate repairs</li>
      <li>Minor body repairs</li>
      <li>Major engine repairs</li>
      <li>Transmission and differentials</li>
      <li>Trailer repairs</li>
      <li>Exhaust repairs</li>
    </ul>
    <div class="photo suv-photo" role="img" aria-label="Photo of a dark grey SUV"></div>
    <div class="strip"></div>
  </div>

  <div class="page right work-page">
    <div class="photo work-photo" role="img" aria-label="Photo of a mechanic holding a wrench in a workshop, with close-up inset views of brake and engine work"></div>
    <div class="right-copy">
      <h2>Professional,<br>High-quality fleet work</h2>
      <p>Make sure your company's fleet of vehicles is something you can be proud of. RoadMedic Services offers diagnostics and repairs from ASE-certified technicians that are trained in the latest software and diagnostic tools. We specialize in maintaining corporate accounts and working with national leasing companies, which is a testament to the high-quality work and attention to detail we offer.</p>
      <ul class="ticks">
        <li><span class="box"><svg><use href="#i-tick"/></svg></span>Scheduled maintenance</li>
        <li><span class="box"><svg><use href="#i-tick"/></svg></span>Engine repair</li>
        <li><span class="box"><svg><use href="#i-tick"/></svg></span>Brake system inspections &amp; repairs</li>
        <li><span class="box"><svg><use href="#i-tick"/></svg></span>Electrical and computer diagnostics</li>
        <li><span class="box"><svg><use href="#i-tick"/></svg></span>Transmission</li>
        <li><span class="box"><svg><use href="#i-tick"/></svg></span>Fuel systems (gas and diesel)</li>
        <li><span class="box"><svg><use href="#i-tick"/></svg></span>Air conditioning and heating</li>
      </ul>
    </div>
    <svg class="band" viewBox="0 0 550 96"><polygon points="0,80 200,80 230,52 550,52 550,96 0,96" fill="url(#g-band)"/><polygon points="0,76 198,76 228,48 550,48 550,52 230,52 200,80 0,80" fill="#5aa9e6"/></svg>
    <div class="phone" style="right:36px;bottom:10px;font-size:24px"><span class="dot" style="width:30px;height:30px"><svg class="icon" style="width:16px;height:16px"><use href="#i-phone"/></svg></span>555 010 2040</div>
  </div>
</section>
</body>
</html>
```